Wedding Startup Full Website Design

We've just completed our online platform and need to create a website that represents our brand and vision, and clearly communicates our features and value proposition to potential users. There are a minimum of 4 pages that need to be designed. One geared toward wedding professionals (venues/vendors/coordinators), another toward engaged couples, one showcasing features, and an 'About Us' page.

The designer will creative freedom to create a unique UI/UX as long as it represents our brand and is relevant to our target audience/market. The ideal candidate will be able to assume the mindset of someone working in the wedding industry and/or an engaged couple. Ability to create illustrations is a plus.

Copy will be provided as needed. We will reimburse for stock images (pending approval before purchasing), but sourcing the stock images will be the responsibility of the designer.

Our current website: https://www.marquiso.com
Updates

Still waiting for a design that stands out from the rest and aligns with the creative brief.

Target Market(s)

Wedding Professionals and Engaged Couples

Industry/Entity Type

Wedding

Number of Pages Required

4 page

Font styles to use
Sans Serif

Colors
ffffff
fbd4d5
f59195
33a6d7
cadf82
86cfc6

Requirements
Must have
• Common sense stuff like having a unified brand that accurately represents our platform, speaks to our target market, and clearly articulates our vision
Nice to have
• Illustrations
Should not have
• Overly cheesy or childish. We want to be professional but still embrace the wedding culture.

```html
<!DOCTYPE html>
<html lang="en">
<head>
<meta charset="utf-8">
<title>Marquiso – Wedding Collaboration Platform</title>
<link rel="stylesheet" href="https://fonts.googleapis.com/css2?family=Poppins:wght@300;400;500;600&family=Pinyon+Script&display=swap">
<style>
:root{
  --white:#ffffff;
  --blush:#fbd4d5;
  --rose:#f59195;
  --sky:#33a6d7;
  --lime:#cadf82;
  --teal:#86cfc6;
  --mint:#e9f9f7;
  --ink:#1e1e1e;
  --text:#6f6f6f;
  --muted:#9a9a9a;
  --dark:#2a2a2a;
  --stage:#efefef;
  --grey-btn:#a8a8a8;
}
*{box-sizing:border-box;margin:0;padding:0}
html,body{width:1200px;height:3495px;overflow:hidden}
body{background:var(--stage);font-family:"Poppins",sans-serif;color:var(--text);position:relative}
.script{font-family:"Pinyon Script",cursive;color:var(--ink);font-weight:400}

/* ---------- desktop layout ---------- */
.desktop{position:absolute;left:28px;top:77px;width:811px;background:var(--white);box-shadow:0 4px 18px rgba(0,0,0,.12)}
.hero{position:relative;height:429px;overflow:hidden;background:linear-gradient(180deg,#efe6de 0%,#e4d9cf 45%,#cdb9a6 100%)}
.hero-photo{position:absolute;inset:0;background:linear-gradient(160deg,rgba(255,255,255,.55),rgba(210,190,170,.35))}
.nav{position:absolute;left:107px;top:28px;width:592px;height:45px;background:var(--white);border-radius:23px;display:flex;align-items:center;padding:0 14px 0 22px;box-shadow:0 2px 8px rgba(0,0,0,.08)}
.brand{font-weight:500;color:var(--sky);font-size:17px;letter-spacing:.2px}
.nav-links{display:flex;gap:22px;margin-left:auto;margin-right:22px;font-size:9.5px;font-weight:500;color:var(--ink)}
.demo-btn{border:1px solid var(--rose);color:var(--rose);font-size:8px;font-weight:500;padding:6px 12px;border-radius:3px;letter-spacing:.4px}
.hero-mark{position:absolute;left:0;right:0;top:150px;text-align:center;font-weight:500;font-size:150px;line-height:1;color:var(--sky);opacity:.9}

.intro{height:310px;display:flex;justify-content:center;gap:110px;padding-top:55px}
.audience{width:170px;text-align:center}
.portrait{width:104px;height:104px;border-radius:50%;margin:0 auto 22px;background:radial-gradient(circle at 50% 60%,#f3d6c4 0 28%,#4a5d78 29% 45%,#f2f2f2 46%)}
.portrait.couple{background:radial-gradient(circle at 50% 60%,#f5c98a 0 28%,#d9534f 29% 45%,#f2f2f2 46%)}
.audience h3{font-size:22px;margin-bottom:10px}
.audience p{font-size:8.5px;line-height:1.65;font-weight:300}

.benefits{height:121px;background:var(--teal);display:flex;justify-content:center;gap:34px;padding-top:30px}
.benefit{width:92px;text-align:center;color:var(--white);font-size:9px;font-weight:500;line-height:1.3}
.benefit svg{display:block;margin:0 auto 8px}

.start{height:287px;background:var(--mint);padding-top:44px}
.start h2{text-align:center;font-size:30px;margin-bottom:32px}
.steps{display:flex;gap:40px;padding-left:107px}
.step{width:180px}
.step-tag{font-size:6px;font-weight:600;color:var(--ink);letter-spacing:.5px;border-bottom:1px solid var(--ink);display:inline-block;padding-bottom:1px}
.step h4{font-size:21px;margin:2px 0 10px}
.step.dim .step-tag,.step.dim h4{color:var(--muted);border-color:var(--muted)}
.step p{font-size:8.5px;line-height:1.6;font-weight:300;min-height:34px}
.step p b{color:var(--ink);font-weight:600;text-decoration:underline}
.btn{display:inline-block;margin-top:14px;background:var(--ink);color:var(--white);font-size:7px;font-weight:600;padding:8px 14px;letter-spacing:.4px}
.step.dim .btn{background:var(--grey-btn)}

.features{height:244px;position:relative}
.device-art{position:absolute;left:107px;top:46px;width:312px;height:135px;background:linear-gradient(180deg,#a6ddd4,#86cfc6)}
.feature-box{position:absolute;left:385px;top:46px;width:345px;height:135px;background:#f2f2f2;padding:16px 18px 0 36px}
.feature-box p{font-size:8px;line-height:1.55;font-weight:300;margin-bottom:9px}
.feature-box b{color:var(--ink);font-weight:600}

.footer{height:170px;background:var(--dark);position:relative;color:#bdbdbd;clip-path:polygon(0 24%,100% 0,100% 100%,0 100%)}
.footer-cols{position:absolute;left:107px;top:56px;display:flex;gap:70px}
.footer h5{color:var(--white);font-size:8px;font-weight:500;letter-spacing:.4px;margin-bottom:8px}
.footer small{display:block;font-size:6.5px;line-height:1.7;font-weight:300}
.signup{width:155px}
.email-field{display:flex;justify-content:space-between;align-items:center;background:var(--white);color:var(--muted);font-size:6.5px;padding:5px 8px;margin-top:8px;border-radius:2px}
.links{display:flex;gap:40px}
.contact-row{display:flex;gap:8px;align-items:flex-start;margin-bottom:4px}
.contact-row svg{flex:none;margin-top:2px}
.footer-base{position:absolute;left:107px;right:81px;bottom:10px;border-top:1px solid #3d3d3d;padding-top:9px;display:flex;justify-content:space-between;align-items:center}
.socials{display:flex;gap:5px}
.socials i{width:12px;height:12px;border-radius:50%;background:#8a8a8a;display:block}

/* ---------- mobile layout ---------- */
.mobile{position:absolute;left:885px;top:154px;width:266px;background:var(--white);box-shadow:0 4px 18px rgba(0,0,0,.12)}
.m-hero{position:relative;height:342px;background:linear-gradient(180deg,#efe6de 0%,#e2d6cb 50%,#cbb6a3 100%)}
.m-nav{position:absolute;left:12px;right:12px;top:26px;height:40px;background:var(--white);border-radius:20px;display:flex;align-items:center;padding:0 10px 0 16px;gap:8px}
.m-nav .brand{font-size:14px;margin-right:auto}
.m-nav .demo-btn{font-size:6.5px;padding:5px 8px}
.burger{width:18px;height:18px;border-radius:50%;background:#eee;display:flex;flex-direction:column;justify-content:center;align-items:center;gap:2px}
.burger i{width:8px;height:1px;background:var(--ink);display:block}
.m-hero .hero-mark{top:130px;font-size:56px}

.m-intro{height:639px;text-align:center;padding-top:50px}
.m-intro .audience{width:210px;margin:0 auto 60px}
.m-intro .portrait{width:100px;height:100px}

.m-benefits{height:559px;background:var(--teal);padding-top:40px}
.m-benefits .benefit{width:auto;margin-bottom:42px;font-size:8px}

.m-start{height:694px;background:var(--mint);padding:40px 0 0 22px}
.m-start h2{font-size:28px;text-align:center;margin:0 22px 34px 0}
.m-start .step{width:220px;margin-bottom:56px}

.m-features{height:431px;padding:30px 22px 0}
.m-features .device-art{position:static;width:222px;height:107px;margin-bottom:14px}
.m-features p{font-size:7.5px;line-height:1.55;font-weight:300;margin-bottom:12px;padding-left:12px}
.m-features b{color:var(--ink);font-weight:600}

.m-footer{height:466px;background:var(--dark);color:#bdbdbd;padding:58px 22px 0;position:relative;clip-path:polygon(0 7%,100% 0,100% 100%,0 100%)}
.m-footer .footer-block{margin-bottom:22px}
.m-footer .email-field{width:222px}
.m-footer .footer-base{left:22px;right:22px;bottom:18px;flex-direction:column;align-items:flex-start;gap:8px}
</style>
</head>
<body>

<!-- Desktop page -->
<main class="desktop">
  <header class="hero">
    <div class="hero-photo" role="img" aria-label="Photo of a wedding ceremony aisle lined with white folding chairs"></div>
    <nav class="nav">
      <span class="brand">Marquiso</span>
      <div class="nav-links"><span>Wedding Professionals</span><span>About Us</span><span>Features</span><span>For Couples</span></div>
      <span class="demo-btn">ACCESS DEMO</span>
    </nav>
    <div class="hero-mark">Marquiso</div>
  </header>

  <section class="intro">
    <article class="audience">
      <div class="portrait" role="img" aria-label="Illustration of a wedding professional at a desk"></div>
      <h3 class="script">For Professional</h3>
      <p>No longer do you have to go through emails, phone records, text messages, and meeting notes in order to piece together all the details for an upcoming event.</p>
    </article>
    <article class="audience">
      <div class="portrait couple" role="img" aria-label="Illustration of an engaged couple sharing a toast"></div>
      <h3 class="script">For Couples</h3>
      <p>No longer do you have to go through emails, phone records, text messages, and meeting notes in order to piece together all the details for an upcoming event.</p>
    </article>
  </section>

  <section class="benefits">
    <div class="benefit"><svg width="26" height="26" viewBox="0 0 26 26"><circle cx="13" cy="13" r="12" fill="#243447"/><circle cx="13" cy="13" r="7" fill="none" stroke="#fff" stroke-width="1.4"/><path d="M13 9v4l3 2" stroke="#fff" stroke-width="1.4" fill="none"/></svg>Saves Everyone Time</div>
    <div class="benefit"><svg width="26" height="26" viewBox="0 0 26 26"><rect width="26" height="26" rx="3" fill="#f2f2f2"/><circle cx="12" cy="10" r="4" fill="#243447"/><path d="M5 21c1-5 13-5 14 0z" fill="#243447"/><path d="M17 6l2 2 4-4" stroke="#7bb661" stroke-width="1.6" fill="none"/></svg>Better Client Review</div>
    <div class="benefit"><svg width="26" height="26" viewBox="0 0 26 26"><rect x="3" y="4" width="20" height="14" fill="#fff" stroke="#243447" stroke-width="1.4"/><rect x="9" y="10" width="7" height="12" fill="#243447"/><path d="M1 20h10" stroke="#243447" stroke-width="2"/></svg>Accessible On Any Device</div>
    <div class="benefit"><svg width="26" height="26" viewBox="0 0 26 26"><rect x="2" y="2" width="22" height="22" rx="3" fill="#b9c2c9"/><path d="M7 9h12M7 13h12M7 17h8" stroke="#fff" stroke-width="1.6"/></svg>Simplified Organization</div>
    <div class="benefit"><svg width="26" height="26" viewBox="0 0 26 26"><rect x="2" y="6" width="20" height="14" rx="2" fill="#243447"/><rect x="5" y="9" width="20" height="14" rx="2" fill="#3e6fa8"/><path d="M5 13h20" stroke="#1c2b3a" stroke-width="2"/></svg>Lower Transaction Fees</div>
  </section>

  <section class="start">
    <h2 class="script">How To Get Started</h2>
    <div class="steps">
      <div class="step"><span class="step-tag">SIGN UP</span><h4 class="script">Sign Up</h4><p>Create a free account on Marquiso to access popular collaboration tools. <b>Get Started</b></p><span class="btn">NEXT STEP</span></div>
      <div class="step dim"><span class="step-tag">COLLABORATE</span><h4 class="script">Collaborate</h4><p>Add clients within the application to better organize and manage event details.</p><span class="btn">NEXT STEP</span></div>
      <div class="step dim"><span class="step-tag">CONNECT</span><h4 class="script">Connect</h4><p>Linking your bank account within Marquiso to allow for seamless payments and transfer.</p><span class="btn">NEXT STEP</span></div>
    </div>
  </section>

  <section class="features">
    <div class="feature-box">
      <p><b>Real Time Collaboration:</b> There are often disconnects in the communication channel. At the core of Marquiso we ensure everyone is updated in real time with event information.</p>
      <p><b>Cloud Storage:</b> No longer do you have to remember where every piece of information is saved. With Marquiso all your information is available in one central location.</p>
      <p><b>Notifications &amp; Deadlines:</b> Every detail is important and matters. Marquiso helps make sure that all the information for an event are inputted and updated in a timely manner.</p>
    </div>
    <div class="device-art" role="img" aria-label="Illustration of hands holding a tablet showing a user profile"></div>
  </section>

  <footer class="footer">
    <div class="footer-cols">
      <div class="signup"><h5>STAY IN TOUCH</h5><small>Sign up here to receive marketing updates</small>
        <div class="email-field">Email Address<svg width="8" height="8" viewBox="0 0 8 8"><path d="M0 4L8 0 6 8 4 5z" fill="#1e1e1e"/></svg></div></div>
      <div><h5>QUICK LINKS</h5><div class="links"><small>Wedding Professionals<br>About Us<br>Features<br>For Couples</small><small>FAQ<br>Contact<br>Privacy Policy</small></div></div>
      <div><h5>CONTACT US</h5>
        <div class="contact-row"><svg width="7" height="7" viewBox="0 0 8 8"><path d="M1 0h2l1 2-1 1c.5 1 1 1.5 2 2l1-1 2 1v2c-4 1-8-3-7-7z" fill="#bdbdbd"/></svg><small>+1 (555) 014-7261</small></div>
        <div class="contact-row"><svg width="7" height="8" viewBox="0 0 8 10"><path d="M4 0a4 4 0 014 4c0 3-4 6-4 6S0 7 0 4a4 4 0 014-4z" fill="#bdbdbd"/></svg><small>118 Orchard Lane, Suite 4<br>Portland, OR 97201</small></div>
        <div class="contact-row"><svg width="8" height="6" viewBox="0 0 8 6"><rect width="8" height="6" fill="#bdbdbd"/><path d="M0 0l4 3 4-3" stroke="#2a2a2a" fill="none"/></svg><small>info@marquiso.com</small></div>
      </div>
    </div>
    <div class="footer-base"><small>Copyright © 2018 Marquiso. All rights reserved.</small><div class="socials"><i></i><i></i><i></i><i></i></div></div>
  </footer>
</main>

<!-- Mobile page -->
<main class="mobile">
  <header class="m-hero">
    <div class="hero-photo" role="img" aria-label="Photo of a wedding ceremony aisle lined with white folding chairs"></div>
    <nav class="m-nav"><span class="brand">Marquiso</span><span class="demo-btn">ACCESS DEMO</span><span class="burger"><i></i><i></i><i></i></span></nav>
    <div class="hero-mark">Marquiso</div>
  </header>

  <section class="m-intro">
    <article class="audience">
      <div class="portrait" role="img" aria-label="Illustration of a wedding professional at a desk"></div>
      <h3 class="script">For Professional</h3>
      <p>No longer do you have to go through emails, phone records, text messages, and meeting notes in order to piece together all the details for an upcoming event.</p>
    </article>
    <article class="audience">
      <div class="portrait couple" role="img" aria-label="Illustration of an engaged couple sharing a toast"></div>
      <h3 class="script">For Couples</h3>
      <p>No longer do you have to go through emails, phone records, text messages, and meeting notes in order to piece together all the details for an upcoming event.</p>
    </article>
  </section>

  <section class="m-benefits">
    <div class="benefit"><svg width="26" height="26" viewBox="0 0 26 26"><circle cx="13" cy="13" r="12" fill="#243447"/><circle cx="13" cy="13" r="7" fill="none" stroke="#fff" stroke-width="1.4"/><path d="M13 9v4l3 2" stroke="#fff" stroke-width="1.4" fill="none"/></svg>Saves Everyone Time</div>
    <div class="benefit"><svg width="26" height="26" viewBox="0 0 26 26"><rect width="26" height="26" rx="3" fill="#f2f2f2"/><circle cx="12" cy="10" r="4" fill="#243447"/><path d="M5 21c1-5 13-5 14 0z" fill="#243447"/><path d="M17 6l2 2 4-4" stroke="#7bb661" stroke-width="1.6" fill="none"/></svg>Better Client Review</div>
    <div class="benefit"><svg width="26" height="26" viewBox="0 0 26 26"><rect x="3" y="4" width="20" height="14" fill="#fff" stroke="#243447" stroke-width="1.4"/><rect x="9" y="10" width="7" height="12" fill="#243447"/><path d="M1 20h10" stroke="#243447" stroke-width="2"/></svg>Accessible On Any Device</div>
    <div class="benefit"><svg width="26" height="26" viewBox="0 0 26 26"><rect x="2" y="2" width="22" height="22" rx="3" fill="#b9c2c9"/><path d="M7 9h12M7 13h12M7 17h8" stroke="#fff" stroke-width="1.6"/></svg>Simplified Organization</div>
    <div class="benefit"><svg width="26" height="26" viewBox="0 0 26 26"><rect x="2" y="6" width="20" height="14" rx="2" fill="#243447"/><rect x="5" y="9" width="20" height="14" rx="2" fill="#3e6fa8"/><path d="M5 13h20" stroke="#1c2b3a" stroke-width="2"/></svg>Lower Transaction Fees</div>
  </section>

  <section class="m-start">
    <h2 class="script">How To Get Started</h2>
    <div class="step"><span class="step-tag">SIGN UP</span><h4 class="script">Sign Up</h4><p>Create a free account on Marquiso to access popular collaboration tools. <b>Get Started</b></p><span class="btn">NEXT STEP</span></div>
    <div class="step dim"><span class="step-tag">COLLABORATE</span><h4 class="script">Collaborate</h4><p>Add clients within the application to better organize and manage event details.</p><span class="btn">NEXT STEP</span></div>
    <div class="step dim"><span class="step-tag">CONNECT</span><h4 class="script">Connect</h4><p>Linking your bank account within Marquiso to allow for seamless payments and transfer.</p><span class="btn">NEXT STEP</span></div>
  </section>

  <section class="m-features">
    <div class="device-art" role="img" aria-label="Illustration of hands holding a tablet showing a user profile"></div>
    <p><b>Real Time Collaboration:</b> There are often disconnects in the communication channel. At the core of Marquiso we ensure everyone is updated in real time with event information.</p>
    <p><b>Cloud Storage:</b> No longer do you have to remember where every piece of information is saved. With Marquiso all your information is available in one central location.</p>
    <p><b>Notifications &amp; Deadlines:</b> Every detail is important and matters. Marquiso helps make sure that all the information for an event are inputted and updated in a timely manner.</p>
  </section>

  <footer class="m-footer footer">
    <div class="footer-block"><h5>STAY IN TOUCH</h5><small>Sign up here to receive marketing updates</small>
      <div class="email-field">Email Address<svg width="8" height="8" viewBox="0 0 8 8"><path d="M0 4L8 0 6 8 4 5z" fill="#1e1e1e"/></svg></div></div>
    <div class="footer-block"><h5>QUICK LINKS</h5><small>Wedding Professionals<br>About Us<br>Features<br>For Couples<br>FAQ<br>Contact<br>Privacy Policy</small></div>
    <div class="footer-block"><h5>CONTACT US</h5>
      <div class="contact-row"><svg width="7" height="7" viewBox="0 0 8 8"><path d="M1 0h2l1 2-1 1c.5 1 1 1.5 2 2l1-1 2 1v2c-4 1-8-3-7-7z" fill="#bdbdbd"/></svg><small>+1 (555) 014-7261</small></div>
      <div class="contact-row"><svg width="7" height="8" viewBox="0 0 8 10"><path d="M4 0a4 4 0 014 4c0 3-4 6-4 6S0 7 0 4a4 4 0 014-4z" fill="#bdbdbd"/></svg><small>118 Orchard Lane, Suite 4<br>Portland, OR 97201</small></div>
      <div class="contact-row"><svg width="8" height="6" viewBox="0 0 8 6"><rect width="8" height="6" fill="#bdbdbd"/><path d="M0 0l4 3 4-3" stroke="#2a2a2a" fill="none"/></svg><small>info@marquiso.com</small></div>
    </div>
    <div class="footer-base"><small>Copyright © 2018 Marquiso. All rights reserved.</small><div class="socials"><i></i><i></i><i></i><i></i></div></div>
  </footer>
</main>

</body>
</html>
```